Property inventory reports of the highest quality for agents

We need a brochure for a residential inventory company providing condition reports at the start and end of tenancy for letting agents and private landlords for our company called Larkfield Reports. Our main target market is high end properties but we do work across the entire portfolio of properties available.

The main services we offer are:

1) Inventory compilation
2) Tenant check in
3) Tenant check out

This brochure should be designed to market to the Agent market alone, we will convert the final brochure to a version for other markets.

Final print ready specification to be confirmed shortly but will be A4 folded 297mm x 210mm and A3 unfolded 420mm x 297 mm with probably a .25inch bleed

Themes to communicate:

1) Quality and detailed reports
2) Easy to use and time saving reports
3) Top quality existing clients and testimonials (see website)
4) Professional and trust worthy
5) Accommodating and flexible

Main objectives of brochure:

1) Addition point of reference for sales messages across other media
2) Convert leads from conferences and booked meetings
3) Convert leads from booked meetings to instructions
4) Encouraging agents to call office number to book meeting or instruction
5) Outline services offered

Target Market(s)

Letting Agents, mainly high end but should appeal to all

Industry/Entity Type

Residential

Requirements
Must have
• 1) Use existing colours and typography from example brochures and corporate material
2) Pictures on exterior and interior pages mainly of quality property interiors
3) Main selling point should be included on cover and interior ‘Saving you time and reducing disputes’
4) Clear and prominent call to action for target market to call and book meeting or instructions

```html
<!DOCTYPE html>
<html lang="en">
<head>
<meta charset="utf-8">
<title>Larkfield Reports – Brochure Spread</title>
<link href="https://fonts.googleapis.com/css2?family=Open+Sans:wght@300;400;600;700&display=swap" rel="stylesheet">
<style>
:root{
  --brand-blue:#1d4f9e;
  --brand-navy:#1a3a82;
  --ink:#333a44;
  --paper:#ffffff;
  --panel:#e6e8ec;
  --backdrop:#eceef1;
  --photo-light:#e9e8e4;
  --photo-mid:#cfcac2;
}
*{margin:0;padding:0;box-sizing:border-box}
html,body{width:1200px;height:900px;overflow:hidden;background:var(--backdrop);font-family:"Open Sans",sans-serif;color:var(--ink)}
.spread{position:absolute;left:30px;top:30px;width:1140px;height:805px;background:var(--paper);overflow:hidden;box-shadow:0 1px 4px rgba(0,0,0,.12)}
.fold{position:absolute;left:560px;top:0;width:30px;height:780px;background:linear-gradient(90deg,rgba(0,0,0,0),rgba(0,0,0,.04),rgba(0,0,0,0))}
.headline{position:absolute;left:60px;top:62px;width:320px;font-size:20.5px;line-height:26px;font-weight:700;color:var(--brand-blue)}
.intro{position:absolute;left:60px;top:146px;width:211px}
.intro p{font-size:8.6px;line-height:11.6px;text-align:justify;margin-bottom:11.5px}
.service-title{position:absolute;left:65px;top:586px;font-size:9px;font-weight:700;color:var(--brand-blue)}
.service-text{position:absolute;left:65px;top:606px;width:210px;font-size:6.4px;line-height:9.2px}
.service-list{position:absolute;top:658px;list-style:none;font-size:6.6px;color:var(--brand-blue)}
.service-list li{position:relative;padding-left:12px;height:11px;line-height:9px}
.service-list li::before{content:"";position:absolute;left:0;top:1px;width:7px;height:7px;background:var(--brand-navy)}
.service-list.first{left:60px}.service-list.second{left:163px}
.hero{position:absolute;left:308px;top:34px}
.photo{position:absolute}
.photo.bath{left:324px;top:391px;width:232px;height:162px;background:linear-gradient(160deg,#ede9e3,#c9c2b8 60%,#5a4f48)}
.photo.lounge{left:324px;top:574px;width:232px;height:156px;background:linear-gradient(180deg,#f1f1ef,#e3e1dc 55%,#8a6a50)}
.photo.kitchen{left:585px;top:391px;width:172px;height:339px;background:linear-gradient(180deg,#f4f4f3,#dedbd6 55%,#3e3a37)}
.column{position:absolute;top:58px;width:136px}
.column.one{left:792px}.column.two{left:952px}
.column h3{font-size:7.6px;font-weight:700;color:var(--brand-blue);margin-bottom:10px}
.column p{font-size:6.2px;line-height:9.2px;text-align:justify;margin-bottom:9px}
.column .block{margin-bottom:14px}
.cta{position:absolute;left:825px;top:425px;width:255px;height:293px}
.cta svg{position:absolute;left:0;top:0}
.cta .call{position:absolute;left:0;width:255px;text-align:center;top:70px;font-size:42px;font-weight:700;color:var(--brand-blue);line-height:46px}
.cta .bar{position:absolute;left:0;top:120px;width:251px;height:28px;background:var(--brand-blue);color:#fff;font-size:13px;font-weight:700;letter-spacing:1.6px;text-align:center;line-height:28px}
.cta .phone{position:absolute;left:0;width:255px;top:154px;text-align:center;font-size:25px;font-weight:700;color:var(--brand-blue)}
.cta .more{position:absolute;left:0;width:255px;top:218px;text-align:center;font-size:15.5px;font-weight:300;line-height:19px;color:var(--brand-blue)}
.cta .web{position:absolute;left:0;width:255px;top:260px;text-align:center;font-size:13.5px;font-weight:700;color:var(--brand-navy)}
.footer-band{position:absolute;left:0;top:782px;width:1140px;height:23px;background:linear-gradient(90deg,var(--brand-blue),#23358a 50%,var(--brand-blue))}
.roof{position:absolute;top:745px}
.roof.left{left:0}.roof.right{left:955px}
</style>
</head>
<body>
<div class="spread">
  <div class="fold"></div>

  <h1 class="headline">The Professionals that provide Facts Not Opinion…</h1>
  <div class="intro">
    <p>Larkfield Reports uses “Facts not Opinion” to protect Landlords’ properties against unfair deposit disputes at the end of each tenancy. Using proven criteria for each measurement, we produce robust and independent inventories to support rightful claims for compensation which can then be used as evidence to support your claim.</p>
    <p>We are independent specialists that have been instructed by letting agencies on behalf of their landlords in the Surrey area for over five years</p>
    <p>Tenancy Deposit Protection (eg. TDR) requires an accurate and robust inventory to be available as evidence in the event of a dispute. It is the objective of Larkfield Reports to provide the clear unequivocal facts that will avoid the need for this external arbitration.</p>
    <p>Our Professionally accredited representatives have both public liability and professional indemnity insurance. They undertake Continuous Professional Development (CPD) and are trained to the highest professional level.</p>
    <p>Unique structured criteria combined with our highly trained staff create accurate inventory information and photographic evidence to assess and apportion responsibilities both during and at the end of each tenancy.</p>
    <p>Continuously updated inventories. Data from the periodic inspections, maintenance and purchases are all recorded via the “Tenancy Log” data base. The original inventory is unaltered in order to retain detailed evidence of the property at the time of check-in..</p>
  </div>
  <h2 class="service-title">Total service at your command</h2>
  <p class="service-text">Before, throughout and at the end of the tenancy, we will protect your landlords’ valuable property investment. You don’t have to worry about a thing, as our accredited staff offer a comprehensive list of services that include…</p>
  <ul class="service-list first">
    <li>Inventory compilations</li><li>Tenants check-in</li><li>Periodic inspections</li><li>Tenancy check-out</li>
  </ul>
  <ul class="service-list second">
    <li>TDR report and deposit advice</li><li>Energy Performance Certificates</li><li>Rigorously updated inventories</li><li>New property snagging advice</li>
  </ul>

  <svg class="hero" width="452" height="340" viewBox="0 0 452 340">
    <defs><linearGradient id="heroFill" x1="0" y1="0" x2="1" y2="1"><stop offset="0" stop-color="#eeeeec"/><stop offset=".6" stop-color="#dcdad6"/><stop offset="1" stop-color="#c3c0ba"/></linearGradient></defs>
    <polygon role="img" aria-label="Photo of a bright white living room with fireplace and corner sofa" points="16,88 319,8 449,86 449,334 16,334" fill="url(#heroFill)"/>
    <polygon points="0,100 319,0 452,90 449,86 319,10 16,90" fill="var(--brand-blue)"/>
  </svg>
  <div class="photo bath" role="img" aria-label="Photo of a modern bathroom vanity with basin"></div>
  <div class="photo lounge" role="img" aria-label="Photo of an open-plan lounge with wooden floor"></div>
  <div class="photo kitchen" role="img" aria-label="Photo of a white kitchen with range cooker"></div>

  <div class="column one">
    <div class="block">
      <h3>Compilation of Inventory</h3>
      <p>Our inventories are produced using clear and unequivocal language with dated digital photography which accurately reflects the content and condition of properties prior to the commencement of each tenancy.</p>
      <p>Using pre-determined structured criteria, the report is prepared, then appraised and approved by both parties. This ensures that agreed standards are set, thus avoiding disputes and debates at the end of the tenancy. An e-mail version or hard copy of the report is supplied along with digital dated photographs.</p>
    </div>
    <div class="block">
      <h3>Checking In Tenants</h3>
      <p>The day on which the new tenancy begins, Larkfield Reports will attend the property and meet with the new tenants. The inventory is checked and endorsed as correct by both the tenant and inventory representative by signing each page and any amendments agreed. Keys are handed over and meter readings recorded. The completed report is then supplied to the agent.</p>
    </div>
    <div class="block">
      <h3>Introducing the Live RecordTM</h3>
      <p>“When a tenancy starts time doesn’t stop!” Information from periodic inspections, maintenance and purchases are all recorded via the “Tenancy Log” data base. The original inventory is unaltered in order to retain detailed evidence of the property at the time of check-in. For you, the Live RecordTM provides an ongoing, fail-safe record of the ever-changing content and condition of the property throughout the tenancy.</p>
    </div>
  </div>
  <div class="column two">
    <h3>Checking out Tenants</h3>
    <p>On the day of check out, Larkfield Reports meets with the tenant at the property, when a thorough assessment of the property is made against the original inventory, and any recorded actions that have been taken throughout the tenancy. The content and condition is endorsed and signed on each page by both parties. Additional supporting photographs are taken, meter readings are recorded and all keys returned. Larkfield Reports will “Assess wear &amp; tear” of the property during the tenancy, “Apportion the costs” of remedial actions against the potential for betterment and “Assign responsibilities” to landlords and tenant’s for the deposit release. So there’s no debate, just unequivocal facts!</p>
  </div>

  <div class="cta">
    <svg width="255" height="293" viewBox="0 0 255 293"><polygon points="0,70 165,0 255,46 255,293 0,293" fill="var(--panel)"/></svg>
    <div class="call">Call Now</div>
    <div class="bar">TO BOOK A MEETING</div>
    <div class="phone">08450 555 274</div>
    <div class="more">for more information<br>visit our website</div>
    <div class="web">www.larkfieldreports.co.uk</div>
  </div>

  <div class="footer-band"></div>
  <svg class="roof left" width="200" height="40" viewBox="0 0 200 40">
    <polygon points="0,37 95,0 195,37" fill="var(--brand-blue)"/>
    <polyline points="22,33 95,8 170,33" fill="none" stroke="#fff" stroke-width="2.5"/>
    <path d="M82,37 v-8 a8,8 0 0 1 16,0 v8z" fill="#fff"/>
    <path d="M90,22 v15 M82,31 h16" stroke="var(--brand-blue)" stroke-width="1.6"/>
  </svg>
  <svg class="roof right" width="185" height="40" viewBox="0 0 185 40">
    <polygon points="0,37 95,0 185,37" fill="var(--brand-blue)"/>
    <polyline points="22,33 95,8 165,33" fill="none" stroke="#fff" stroke-width="2.5"/>
    <path d="M87,37 v-8 a8,8 0 0 1 16,0 v8z" fill="#fff"/>
    <path d="M95,22 v15 M87,31 h16" stroke="var(--brand-blue)" stroke-width="1.6"/>
  </svg>
</div>
</body>
</html>
```